Brindle Outcomes WebDesign

Although the designs we have had are great we are looking for something unique and would like to move away from the traditional. We append additional comments and files to reflect this. WE are looking for designs to showcase there artistic flare.

Task
To design Brindle Outcomes home page and a second page ie information on our Internet Marketing Services

Client:
Brindle Outcomes is the next generation provider of international marketing, branding, design, Search Engine Optimization(SEO) and Search Engine Marketing(SEM). Utilising a variety of crowd-source channels and trust networks, Brindle Outcomes is able to offer you a complete internet marketing package. From initial design and branding to the continued work on SEO all our services are geared towards dramatically increasings your revenues. Our primary goal is to build greater trading bridges between English-speaking and Chinese-speaking worlds. We believe that a true understanding of the local market is only achievable if you are a native speaker. The power of our networks and processes have been focused to enable Brindle Outcomes to enlist only native speakers to bolster your Internet Marketing Campaign.

The primary color pallet is:

FF9571
B23308
FF6633
858585
BDBDBD
or
https://palettes.vormix.example/#themes/search?term=brindle%20outcomes

Sites we like
http://www.trevonix.example/
http://www.morbela.example/
Updates

We have believe that we will need to push our design packages (outsourced through artflockly) more. We would like this to be reflected on the front page.

This means that the menu should also include

Design
Also the use of content management system wendix

Have added a few more sites that we like
www.harbourpixelstudio.example.hk
www.qmt.example.hk

Really excited with all the designs so far.  We would like the design to move away from the more standard layout. With this in mind we would like to see some design that feature hexagons, or decagons.
Please feel free to let loose! we want a design that is quit unique

We have included to vector files.

vector file 8016151 is for a color reference we thik that in order to enhence the design we need to expand the color palette, would want to maintain the primary corporate colors, but include some bright additional colors.

The second was our insipration for the the hexagon. expanding on the idea we thought that the main menu could be made up of hexagons. The ad/info modules that appear half way up the page be similar to those in the vector.

Reason: Have updated brief and are looking for a more unique feel to the design.

Target Market(s)

Small to medium business looking to branch out further in the international market

Industry/Entity Type

Internet

Requirements
Must have
• A login/search section
A separate floating feedback tab
Main Navigation – Home, Internet Marketing, Cloud Computing
A banner space from informative text on our services
Must have a request for a quote on each page

```html
<!DOCTYPE html>
<html lang="en">
<head>
<meta charset="utf-8">
<title>Brindle Outcomes — SEO and Cloud Consultant</title>
<link href="https://fonts.googleapis.com/css2?family=Anton&family=Open+Sans:wght@400;600;700&family=Lato:wght@400;700&display=swap" rel="stylesheet">
<style>
:root{
  --paper:#d6c3a8;
  --orange:#ff6633;
  --orange-deep:#e8582a;
  --amber:#f39a12;
  --red:#e53a2e;
  --red-dark:#b2161e;
  --rust:#b23308;
  --grey:#858585;
  --grey-light:#bdbdbd;
  --ink:#222;
  --body:#444;
  --link:#1b5fa8;
}
*{margin:0;padding:0;box-sizing:border-box}
html,body{width:1003px;height:1200px;overflow:hidden}
body{position:relative;background:var(--paper);font-family:"Open Sans",Arial,sans-serif;color:var(--body)}
.shapes{position:absolute;left:0;top:0}
.abs{position:absolute}
.header-band{position:absolute;left:0;top:0;width:1003px;height:96px;background:linear-gradient(#fff,#ececec);border-bottom:2px solid #9a9a9a}
.brand{position:absolute;left:199px;top:23px;font-family:"Lato",Arial,sans-serif;font-weight:700;font-size:27px;color:var(--orange-deep);letter-spacing:-.6px}
.tagline{position:absolute;left:228px;top:57px;font-size:10px;font-weight:600;color:#222}
.nav-label{position:absolute;color:#fff;font-family:"Lato",Arial,sans-serif;font-weight:700;line-height:16px}
.call{position:absolute;right:119px;top:5px;font-family:"Lato",Arial,sans-serif;font-size:15px;color:#333}
.call b{color:var(--orange);font-size:16px;font-weight:700}
.login{position:absolute;left:822px;top:33px;width:62px;height:22px;background:linear-gradient(#c22a20,#8e1410);border-radius:3px;color:#fff;font-size:11px;font-weight:700;padding:4px 0 0 23px}
.search{position:absolute;left:711px;top:68px;width:174px;height:24px;background:#fff;border:1px solid #ccc;border-radius:3px;font-size:10px;color:#888;padding:5px 0 0 8px}
.search svg{position:absolute;right:5px;top:4px}
.hex-title{position:absolute;font-family:"Anton",Impact,sans-serif;font-weight:400;color:var(--ink);font-size:19px;line-height:18px}
.hex-body{position:absolute;font-size:10.5px;line-height:14.2px;color:var(--body)}
.read-more{position:absolute;font-size:10px;color:var(--rust);text-align:center;width:70px}
.read-more::after{content:"";display:block;margin:2px auto 0;width:0;height:0;border:4px solid transparent;border-top-color:#888;border-bottom:0}
.quote{position:absolute;left:657px;top:172px;width:228px;height:287px;background:#f4f1ec;border:1px solid #d2cfc9;border-radius:4px;box-shadow:0 1px 3px rgba(0,0,0,.2)}
.quote h2{font-family:"Lato",Arial,sans-serif;font-weight:400;font-size:18px;color:#222;margin:10px 0 0 14px}
.field{position:absolute;left:14px;width:199px;height:26px;background:#fff;border:1px solid #d4d0ca;border-radius:4px;font-size:10.5px;color:#333;padding:5px 8px}
.submit{position:absolute;left:14px;top:238px;width:199px;height:33px;background:linear-gradient(#ff7a3c,#ef4a10);border-radius:4px;color:#fff;font-family:"Lato",Arial,sans-serif;font-size:24px;text-align:center;line-height:33px;box-shadow:0 2px 0 #333}
.blog-date{font-size:10.5px;color:#777;margin-bottom:4px}
.blog-link{font-size:10.5px;color:var(--link);line-height:14px}
.blog-text{font-size:10.5px;line-height:14px;color:#444}
.blog-rule{border-top:1px solid #ccc;margin:8px 0 9px}
.chat-label{position:absolute;left:598px;top:1106px;width:42px;text-align:center;font-family:"Lato",Arial,sans-serif;font-weight:700;font-size:12px;line-height:12px;color:#222}
.follow{position:absolute;left:662px;top:1093px;font-size:10.5px;color:#333}
.net{position:absolute;font-size:6.5px;font-weight:700;color:var(--grey);text-align:center;width:32px}
.footer-rule{position:absolute;left:0;top:1163px;width:1003px;border-top:1px solid #f3ece2}
.copyright{position:absolute;left:116px;top:1172px;font-size:10.5px;color:#222}
</style>
</head>
<body>
<div class="header-band"></div>

<svg class="shapes" width="1003" height="1200" viewBox="0 0 1003 1200">
  <defs>
    <linearGradient id="redRim" x1="0" y1="0" x2="0" y2="1"><stop offset="0" stop-color="#f0442f"/><stop offset="1" stop-color="#b2161e"/></linearGradient>
    <linearGradient id="greyRim" x1="0" y1="0" x2="0" y2="1"><stop offset="0" stop-color="#dcdcdc"/><stop offset="1" stop-color="#858585"/></linearGradient>
    <linearGradient id="orangeRim" x1="0" y1="0" x2="0" y2="1"><stop offset="0" stop-color="#ff9571"/><stop offset="1" stop-color="#ff6633"/></linearGradient>
    <linearGradient id="amberNav" x1="0" y1="0" x2="0" y2="1"><stop offset="0" stop-color="#ffa516"/><stop offset="1" stop-color="#e58608"/></linearGradient>
    <linearGradient id="darkNav" x1="0" y1="0" x2="0" y2="1"><stop offset="0" stop-color="#7a7a7a"/><stop offset="1" stop-color="#474747"/></linearGradient>
    <radialGradient id="medallionTone" cx=".5" cy=".5" r=".5"><stop offset="0" stop-color="#5fb3e0"/><stop offset=".55" stop-color="#b9dcef"/><stop offset="1" stop-color="#ffffff"/></radialGradient>
  </defs>

  <!-- logo circle -->
  <circle cx="147" cy="45" r="28" fill="none" stroke="#ef5a28" stroke-width="5"/>

  <!-- navigation hexagons -->
  <polygon points="480,86 494,57 524,57 538,86 524,115 494,115" fill="#e33a2f"/>
  <polygon points="517,45 541,3 591,3 615,45 591,87 541,87" fill="url(#darkNav)"/>
  <polygon points="591,86 617,40 671,40 697,86 671,132 617,132" fill="url(#amberNav)"/>

  <!-- feature medallion -->
  <circle cx="707" cy="681" r="178" fill="#fff"/>
  <circle cx="707" cy="681" r="165" fill="url(#medallionTone)" role="img" aria-label="Illustration of a globe wrapped in a network of orbiting lines"/>

  <!-- Internet marketing services -->
  <polygon points="262,106 380,174 380,310 262,378 144,310 144,174" fill="url(#redRim)"/>
  <polygon points="262,122 365,182 365,302 262,362 159,302 159,182" fill="#fff" stroke="#a3121a" stroke-width="3"/>
  <!-- search signal -->
  <polygon points="527,264 643,330 643,464 527,530 411,464 411,330" fill="url(#greyRim)"/>
  <polygon points="527,280 630,338 630,456 527,514 424,456 424,338" fill="#ececec" stroke="#6d6d6d" stroke-width="3"/>
  <!-- what we do -->
  <polygon points="412,538 488,581 488,667 412,710 336,667 336,581" fill="url(#orangeRim)"/>
  <polygon points="412,551 476,588 476,660 412,697 348,660 348,588" fill="#ededed" stroke="#a3121a" stroke-width="3"/>
  <!-- who we are -->
  <polygon points="337,674 416,719 416,809 337,854 258,809 258,719" fill="url(#greyRim)"/>
  <polygon points="337,688 404,726 404,802 337,840 270,802 270,726" fill="#ececec" stroke="#6d6d6d" stroke-width="3"/>
  <!-- recent blogs -->
  <polygon points="415,812 558,894 558,1060 415,1142 272,1060 272,894" fill="url(#redRim)"/>
  <polygon points="415,829 543,903 543,1051 415,1125 287,1051 287,903" fill="#fff" stroke="#a3121a" stroke-width="3"/>

  <!-- connector curves -->
  <g fill="none" stroke="#333" stroke-width="1">
    <path d="M356,151 C330,140 305,150 300,170"/>
    <path d="M402,342 C425,330 440,345 440,356"/>
    <path d="M486,566 C460,560 432,568 428,585"/>
    <path d="M422,724 C405,715 380,720 375,738"/>
    <path d="M548,876 C520,872 503,888 498,905"/>
  </g>

  <!-- icon hexagons -->
  <g fill="#fff" stroke="#ff6633" stroke-width="3">
    <polygon points="380,106 408,122 408,156 380,172 352,156 352,122"/>
    <polygon points="380,314 408,330 408,364 380,380 352,364 352,330"/>
    <polygon points="496,516 524,532 524,566 496,582 468,566 468,532"/>
    <polygon points="446,706 474,722 474,756 446,772 418,756 418,722"/>
    <polygon points="557,825 585,841 585,875 557,891 529,875 529,841"/>
    <polygon points="589,1064 606,1073 606,1091 589,1100 572,1091 572,1073"/>
    <polygon points="619,1090 647,1106 647,1140 619,1156 591,1140 591,1106"/>
  </g>
  <g fill="#fff" stroke="#858585" stroke-width="2">
    <polygon points="669,1111 686,1121 686,1141 669,1151 652,1141 652,1121"/>
    <polygon points="706,1111 723,1121 723,1141 706,1151 689,1141 689,1121"/>
    <polygon points="688,1145 705,1155 705,1175 688,1185 671,1175 671,1155"/>
  </g>

  <!-- icons -->
  <g fill="#555">
    <circle cx="380" cy="139" r="12" fill="none" stroke="#555" stroke-width="6" stroke-dasharray="4 3"/>
    <circle cx="380" cy="139" r="9" fill="none" stroke="#555" stroke-width="4"/>
    <circle cx="376" cy="343" r="7" fill="none" stroke="#555" stroke-width="3"/>
    <line x1="371" y1="348" x2="364" y2="356" stroke="#555" stroke-width="4"/>
    <rect x="383" y="340" width="18" height="9" fill="#999"/>
    <rect x="482" y="538" width="28" height="20" rx="2" fill="none" stroke="#555" stroke-width="2"/>
    <rect x="486" y="543" width="8" height="6"/>
    <rect x="497" y="543" width="10" height="2"/><rect x="497" y="547" width="10" height="2"/><rect x="486" y="552" width="21" height="2"/>
    <circle cx="434" cy="731" r="3.5"/><rect x="430" y="736" width="8" height="13" rx="2"/>
    <circle cx="446" cy="728" r="4"/><rect x="441" y="734" width="10" height="16" rx="2"/>
    <circle cx="458" cy="731" r="3.5"/><rect x="454" y="736" width="8" height="13" rx="2"/>
    <polygon points="541,852 568,842 568,872 541,862"/>
    <rect x="536" y="851" width="7" height="12"/>
    <ellipse cx="589" cy="1081" rx="8" ry="6" fill="none" stroke="#555" stroke-width="1.6"/>
  </g>
</svg>

<div class="brand">BrindleOutcomes.com</div>
<div class="tagline">SEO and Cloud Consultant</div>

<nav>
  <div class="nav-label" style="left:489px;top:78px;font-size:14px">Home</div>
  <div class="nav-label" style="left:531px;top:28px;font-size:14px;text-align:center">Internet<br>Marketing</div>
  <div class="nav-label" style="left:606px;top:72px;font-size:14px">Cloud<br>Computing</div>
</nav>

<div class="call">Call Us Today: <b>186.5550.1927</b></div>
<div class="login">Login</div>
<div class="search">Search
  <svg width="14" height="14" viewBox="0 0 14 14"><circle cx="6" cy="6" r="4.5" fill="none" stroke="#111" stroke-width="2"/><line x1="9" y1="9" x2="13" y2="13" stroke="#111" stroke-width="2.5"/></svg>
</div>

<section>
  <h2 class="hex-title" style="left:181px;top:176px">Our<br>Internet Marketing<br>Services</h2>
  <p class="hex-body" style="left:183px;top:234px;width:160px">Lorem ipsum dolor sit amet, consectetur adipisicing elit, sed do eiusmod tempor incididunt ut labore et dolore magna aliqua.</p>
  <div class="read-more" style="left:227px;top:322px">READ MORE</div>

  <h2 class="hex-title" style="left:447px;top:338px">SearchSignal</h2>
  <p class="hex-body" style="left:447px;top:366px;width:162px">Lorem ipsum dolor sit amet, consectetur adipisicing elit, sed do eiusmod tempor incididunt ut labore et dolore magna aliqua. Ut enim ad minim veniam, quis nostrud exercitation.</p>
  <div class="read-more" style="left:493px;top:477px">READ MORE</div>

  <h2 class="hex-title" style="left:361px;top:585px">What We Do</h2>
  <p class="hex-body" style="left:362px;top:609px;width:118px">Lorem ipsum dolor sit amet, consectetur adipisicing elit, sed do eiusmod tempor...</p>

  <h2 class="hex-title" style="left:278px;top:724px">Who We Are</h2>
  <p class="hex-body" style="left:278px;top:748px;width:120px">Lorem ipsum dolor sit amet, consectetur adipisicing elit, sed do eiusmod tempor...</p>

  <h2 class="hex-title" style="left:362px;top:866px">Recent Blogs</h2>
  <div class="abs" style="left:310px;top:903px;width:207px">
    <div class="blog-date">29-11-2012</div>
    <div class="blog-link">Morbi fringilla enim non velit vehicula mattis.</div>
    <div class="blog-text">Lorem ipsum dolor sit amet, consectetur adipisicing elit.</div>
    <div class="blog-rule"></div>
    <div class="blog-date">28-11-2012</div>
    <div class="blog-link">Morbi fringilla enim non velit vehicula .</div>
    <div class="blog-text">Lorem ipsum dolor sit amet, consectetur adipisicing elit.</div>
  </div>
  <div class="read-more" style="left:382px;top:1087px">READ MORE</div>
</section>

<form class="quote">
  <h2>Request for a quote</h2>
  <div class="field" style="top:54px">Name</div>
  <div class="field" style="top:88px">Email Address</div>
  <div class="field" style="top:122px">Phone Number</div>
  <div class="field" style="top:156px;height:74px">Massage</div>
  <div class="submit">Submit</div>
</form>

<div class="chat-label">CHAT WITH US</div>
<div class="follow">Follow Us</div>
<div class="net" style="left:653px;top:1128px">Plaza</div>
<div class="net" style="left:690px;top:1128px">Chirp</div>
<div class="net" style="left:672px;top:1162px">Linkr</div>

<div class="footer-rule"></div>
<div class="copyright">© BrindleOutcomes 2012</div>
</body>
</html>
```